OLU58 biz card & Stationery

LU58 is a personalized shopping experience brought to you, that lets you find and discover fashion goods through a collection of boutiques curated by taste-makers - celebrities, stylists, designers, and fashion bloggers. Boutiques uses visual technology to help fashionistas discover and shop their look and creates the opportunity for designers to showcase their collections and latest inspirations online.

OLU58 is built on technology developed by our team of fashion experts who work with engineers to “teach” our computer systems to understand various patterns, pairings, and genre definitions. When signed into your account, OLU58 learns about your style and preferences and in turn, provides you better results and recommendations over time. Ultimately, OLU58 will provide shoppers with a much richer and interactive shopping experience and help drive traffic to retailers' websites.

We need a definitely cool business card. The card must be black! And must use our official logo which can be download from OLU58.com

The address for Letter head and evenlop, please use 4872 Crestwick Parkway, Sutie 510 Los Angeles CA90412, email will be anyone@OLU58.com, website is www.OLU58.com

thanks

We received some of the design, thanks. But most of the design are not what we want. We need a very clean version with black ground, you may also use some dark gray to add the element. please take a look at http://morvalstudio.no/work/#pelter__ostrama/, we do like this kind of design very much. hope it help.

```html
<!DOCTYPE html>
<html lang="en">
<head>
<meta charset="utf-8">
<title>OLU58 Business Card &amp; Stationery</title>
<link href="https://fonts.googleapis.com/css2?family=Marcellus&family=Tinos&display=swap" rel="stylesheet">
<style>
  :root {
    --backdrop: #e3dfdf;
    --paper: #ffffff;
    --ink: #000000;
    --charcoal: #2f2f2f;
    --stripe: #666666;
    --light: #ffffff;
    --muted: #bdbdbd;
    --window: #e2f0ef;
    --brand-font: "Marcellus", "Optima", serif;
    --body-font: "Tinos", "Times New Roman", serif;
  }
  * { margin: 0; padding: 0; box-sizing: border-box; }
  html, body { width: 1200px; height: 900px; overflow: hidden; }
  body { background: var(--backdrop); position: relative; font-family: var(--brand-font); }

  .vertical { writing-mode: vertical-rl; transform: rotate(180deg); position: absolute; white-space: nowrap; }

  /* Business card — front */
  .card { position: absolute; width: 239px; height: 136px; background: var(--ink); overflow: hidden; }
  .card--front { left: 26px; top: 224px; }
  .card--back { left: 293px; top: 224px; }
  .card__panel { position: absolute; top: 0; left: 134px; width: 105px; height: 100%; background: var(--charcoal); }
  .card__stripe { position: absolute; top: 0; left: 123px; width: 11px; height: 100%; background: var(--stripe); }
  .card__name { left: 11px; top: 8px; height: 120px; font-size: 7.5px; letter-spacing: 1px; color: var(--light); text-align: start; }
  .card__contact { position: absolute; left: 32px; top: 45px; font-size: 5.4px; line-height: 7.6px; color: var(--muted); }
  .card__contact b { color: var(--light); font-weight: normal; }
  .card__contact .gap { display: block; height: 3px; }
  .card__web { left: 124px; top: 35px; height: 70px; font-size: 6px; color: var(--light); text-align: start; line-height: 9px; }
  .brand { color: var(--light); font-weight: normal; line-height: 1; }
  .card__brand { position: absolute; left: 144px; top: 46px; font-size: 23px; }
  .card__tagline { position: absolute; left: 145px; top: 73px; font-size: 5px; letter-spacing: .4px; color: var(--muted); }
  .card--back .card__brand { left: 0; width: 100%; top: 48px; text-align: center; }
  .card--back .card__tagline { left: 0; width: 100%; top: 76px; text-align: center; }

  /* Envelope */
  .envelope { position: absolute; left: 26px; top: 416px; width: 504px; height: 260px; background: var(--paper); }
  .envelope__header { position: absolute; left: 13px; top: 12px; height: 34px; display: flex; }
  .envelope__brand { width: 85px; background: var(--charcoal); font-size: 20px; display: flex; align-items: center; justify-content: center; }
  .envelope__address { width: 129px; background: var(--ink); color: var(--light); font-family: var(--body-font); font-size: 7.6px; line-height: 9.5px; padding: 5px 0 0 10px; }
  .envelope__window { position: absolute; left: 65px; top: 149px; width: 302px; height: 75px; background: var(--window); border-radius: 10px; }

  /* Letterhead */
  .letterhead { position: absolute; left: 612px; top: 57px; width: 562px; height: 791px; background: var(--paper); }
  .letterhead__stripe { position: absolute; left: 492px; top: 0; width: 8px; height: 100%; background: var(--stripe); }
  .letterhead__band { position: absolute; left: 500px; top: 0; width: 62px; height: 100%; background: var(--ink); }
  .letterhead__tagline { left: 523px; top: 118px; height: 168px; font-size: 12px; letter-spacing: .3px; color: var(--muted); text-align: center; line-height: 16px; }
  .letterhead__brand { left: 512px; top: 345px; height: 100px; font-size: 33px; text-align: center; line-height: 36px; }
  .letterhead__address { left: 518px; top: 520px; height: 146px; font-family: var(--body-font); font-size: 8.8px; line-height: 12.5px; color: var(--light); text-align: start; }
  .letterhead__web { position: absolute; left: 0; width: 492px; top: 741px; text-align: center; color: var(--ink); font-family: var(--brand-font); }
  .letterhead__web .small { font-size: 12px; }
  .letterhead__web .name { font-size: 23px; }
</style>
</head>
<body>

  <section class="card card--front" aria-label="Business card front">
    <div class="card__panel"></div>
    <div class="card__stripe"></div>
    <p class="vertical card__name">DANIEL ROSS WARREN</p>
    <p class="card__contact">
      4872 Crestwick Parkway<br>
      Suite 510 Los Angeles CA90412
      <span class="gap"></span>
      +1 <b>310 555 0148</b><br>
      anyone@<b>OLU58</b>.com
    </p>
    <p class="vertical card__web">www.OLU58.com</p>
    <p class="brand card__brand">OLU58</p>
    <p class="card__tagline">SOCIAL FASHION ONLINE</p>
  </section>

  <section class="card card--back" aria-label="Business card back">
    <p class="brand card__brand">OLU58</p>
    <p class="card__tagline">SOCIAL FASHION ONLINE</p>
  </section>

  <section class="envelope" aria-label="Envelope">
    <div class="envelope__header">
      <div class="brand envelope__brand">OLU58</div>
      <div class="envelope__address">4872 Crestwick Parkway<br>Suite 510 Los Angeles CA90412</div>
    </div>
    <div class="envelope__window"></div>
  </section>

  <section class="letterhead" aria-label="Letterhead">
    <div class="letterhead__stripe"></div>
    <div class="letterhead__band"></div>
    <p class="vertical letterhead__tagline">SOCIAL FASHION ONLINE</p>
    <p class="vertical brand letterhead__brand">OLU58</p>
    <p class="vertical letterhead__address">4872 Crestwick Parkway<br>Suite 510 Los Angeles CA90412</p>
    <p class="letterhead__web"><span class="small">www·</span><span class="name">OLU58</span><span class="small">·COM</span></p>
  </section>

</body>
</html>
```